Business Card Design Needed

Business car design required, logo will be supplied.

Brackenfield Heat Surveyors are looking to become the leading provider of energy performance certificates to estate agents, landlords and home owners in the Yorkshire region of the UK.

The business card must be double sided and professional looking. Estate agents receive hundreds of cards from contractors and our card must stand out.

I require a two sided business card that is clean, modern and created by a designer that can think outside of the box.

Brand colours can be supplied .

Please ask if you have any questions.

Target Market(s)

Estate agents, landlords and property owners

Industry/Entity Type

Property - estate agency - energy consultants

Contact Information for Business Card

Tomas Birchwell - Energy Assessor - 07351642170 - www.BrackenfieldHSV.co.uk - info@brackenfieldhsv.co.uk

Font styles to use
Serif
Sans Serif

Colors
00AB8E
00BBA5
67D7C9
C6EFE9
E9F9F6

Requirements
Must have
• Use the provided logo, clean, professional and stand out from the crowd
Nice to have
• Clever use of text, spacing and brand colours
Should not have
• Clip art

```html
<!DOCTYPE html>
<html lang="en">
<head>
<meta charset="utf-8">
<title>Brackenfield Heat Surveyors – Business Card</title>
<link rel="stylesheet" href="https://fonts.googleapis.com/css2?family=Open+Sans:wght@400;600;700&family=Poppins:wght@300&display=swap">
<style>
  :root {
    --card-blue: #1A77DD;
    --accent-lime: #B4FF0A;
    --page-bg: #ffffff;
  }
  html, body {
    margin: 0;
    padding: 0;
    width: 1200px;
    height: 686px;
    overflow: hidden;
    background: var(--page-bg);
  }
  .card {
    position: relative;
    width: 1200px;
    height: 686px;
    background: var(--card-blue);
    border-radius: 46px;
    color: var(--accent-lime);
    font-family: "Open Sans", Arial, sans-serif;
  }
  .brand-mark {
    position: absolute;
    left: 182px;
    top: 160px;
    width: 156px;
    height: 156px;
    border-radius: 50%;
    background: var(--accent-lime);
  }
  .brand-divider {
    position: absolute;
    left: 375px;
    top: 162px;
    width: 2px;
    height: 152px;
    background: var(--accent-lime);
  }
  .brand-name {
    position: absolute;
    left: 428px;
    top: 168px;
    margin: 0;
    font-family: "Poppins", Arial, sans-serif;
    font-weight: 300;
    color: var(--accent-lime);
    line-height: 1;
  }
  .brand-name .line-main {
    display: block;
    font-size: 74px;
    letter-spacing: 1px;
  }
  .brand-name .line-sub {
    display: block;
    margin-top: 22px;
    font-size: 22px;
    letter-spacing: 12.5px;
  }
  .person {
    position: absolute;
    left: 138px;
    top: 440px;
    width: 400px;
    text-align: center;
  }
  .person-name {
    margin: 0;
    font-size: 40px;
    font-weight: 700;
    line-height: 1.1;
    letter-spacing: 0.5px;
  }
  .person-role {
    margin: 10px 0 0;
    font-size: 31px;
    font-weight: 600;
    letter-spacing: 3px;
    line-height: 1.1;
  }
  .contact-list {
    position: absolute;
    left: 567px;
    top: 406px;
    margin: 0;
    padding: 0;
    list-style: none;
  }
  .contact-item {
    display: flex;
    align-items: center;
    height: 48px;
    margin-bottom: 4.5px;
    font-size: 32px;
    font-weight: 400;
  }
  .contact-icon {
    width: 48px;
    height: 48px;
    margin-right: 14px;
    flex: none;
  }
</style>
</head>
<body>
  <div class="card">
    <div class="brand-mark" aria-hidden="true"></div>
    <div class="brand-divider" aria-hidden="true"></div>
    <h1 class="brand-name">
      <span class="line-main">BRACKENFIELD</span>
      <span class="line-sub">HEAT SURVEYORS</span>
    </h1>

    <div class="person">
      <p class="person-name">TOMAS BIRCHWELL</p>
      <p class="person-role">Energy Assessor</p>
    </div>

    <ul class="contact-list">
      <li class="contact-item">
        <svg class="contact-icon" viewBox="0 0 48 48" aria-hidden="true">
          <circle cx="24" cy="24" r="24" fill="var(--accent-lime)"/>
          <path d="M16 13c1.5-1 3-.6 3.8.8l2 3.6c.6 1.2.3 2.3-.8 3l-1.4 1c1 2.6 3.2 4.9 5.9 6l1-1.4c.8-1 1.9-1.3 3-.7l3.6 2c1.3.8 1.7 2.3.8 3.8l-1 1.5c-1 1.4-3 2-5 1.3-6.6-2.3-11.8-7.6-14-14-.7-2 0-3.9 1.4-5z" fill="var(--card-blue)"/>
          <path d="M27 13a9 9 0 0 1 8 8M27 17.5a4.6 4.6 0 0 1 3.6 3.6" fill="none" stroke="var(--card-blue)" stroke-width="2" stroke-linecap="round"/>
        </svg>
        <span>074 3516 42170</span>
      </li>
      <li class="contact-item">
        <svg class="contact-icon" viewBox="0 0 48 48" aria-hidden="true">
          <circle cx="24" cy="24" r="24" fill="var(--accent-lime)"/>
          <rect x="11" y="15" width="26" height="18" rx="1.5" fill="none" stroke="var(--card-blue)" stroke-width="2.4"/>
          <path d="M11.5 16 24 26l12.5-10M11.5 32.5l9-8M36.5 32.5l-9-8" fill="none" stroke="var(--card-blue)" stroke-width="2.2" stroke-linejoin="round"/>
        </svg>
        <span>info@brackenfieldhsv.co.uk</span>
      </li>
      <li class="contact-item">
        <svg class="contact-icon" viewBox="0 0 48 48" aria-hidden="true">
          <circle cx="24" cy="24" r="24" fill="var(--accent-lime)"/>
          <g fill="none" stroke="var(--card-blue)" stroke-width="2">
            <circle cx="24" cy="24" r="12"/>
            <ellipse cx="24" cy="24" rx="5.5" ry="12"/>
            <path d="M12 24h24M14 18h20M14 30h20M24 12v24"/>
          </g>
        </svg>
        <span>www.BrackenfieldHSV.co.uk</span>
      </li>
    </ul>
  </div>
</body>
</html>
```